Business card design needed

Want the logo on a medium blue background and a nice funky design. I have my own gym and run one on one personal training and nutrition sessions. want it to look lively.
Updates

Please note I requested my logo on a blue background 

PLEASE NOTE: I already have a logo. It is attached to the order!!

Target Market(s)

over 55s

Industry/Entity Type

Nutrition

Contact Information for Business Card

Front of card : Logo ( on blue background )
Corinne Dalby
Nutrition & Fitness Coach for Seniors
Private gym at : 17 Fennick Street, Brantwood, Perth, WA 6291
Mob : 0412736158
Email : corinnedalby@fernpost.example
"For Seniors by a Senior"

Back of card
B.A. ( Soc.)
Dip. Ed. (Sec.)
Wellness Coach
Cert 4 Personal Trainer
Cert. Nutritition
MOVE ON Facilitator
Ageing Well Moving Freely Facilitator
NLP Master

```html
<!DOCTYPE html>
<html lang="en">
<head>
<meta charset="utf-8">
<title>Evergreen Nutrition &amp; Fitness – Business Card</title>
<link href="https://fonts.googleapis.com/css2?family=Open+Sans:wght@400;600&display=swap" rel="stylesheet">
<style>
  :root {
    --backdrop: #000000;
    --card-blue: #035a8c;
    --panel-white: #ffffff;
    --ink-blue: #1a5a8f;
    --ink-white: #ffffff;
  }
  html, body {
    margin: 0;
    padding: 0;
    width: 1200px;
    height: 1000px;
    overflow: hidden;
    background: var(--backdrop);
    font-family: "Open Sans", "Segoe UI", Arial, sans-serif;
  }
  .canvas {
    position: relative;
    width: 1200px;
    height: 1000px;
  }
  .card {
    position: absolute;
    left: 231px;
    width: 721px;
    height: 445px;
    background: var(--card-blue);
  }
  .card--front { top: 46px; }
  .card--back { top: 517px; }

  .info-panel {
    position: absolute;
    left: 49px;
    top: 125px;
    width: 627px;
    height: 187px;
    background: var(--panel-white);
    box-shadow: 5px 6px 6px rgba(0, 0, 0, 0.55);
    display: flex;
    align-items: center;
  }
  .brand {
    width: 230px;
    padding-left: 20px;
    box-sizing: border-box;
    display: flex;
    align-items: center;
    gap: 10px;
    color: var(--card-blue);
    font-weight: 600;
    font-size: 21px;
    line-height: 1.25;
  }
  .brand__dot {
    flex: 0 0 auto;
    width: 18px;
    height: 18px;
    border-radius: 50%;
    background: var(--card-blue);
  }
  .contact {
    margin-left: 15px;
    width: 375px;
    color: var(--ink-blue);
    font-size: 17.5px;
    line-height: 27.5px;
  }
  .contact p { margin: 0; }

  .credentials-frame {
    position: absolute;
    left: 48px;
    top: 125px;
    width: 628px;
    height: 188px;
    box-sizing: border-box;
    border: 2px solid var(--ink-white);
    display: flex;
    align-items: center;
    justify-content: center;
  }
  .credentials {
    margin: 0;
    width: 560px;
    text-align: center;
    color: var(--ink-white);
    font-size: 17.5px;
    line-height: 27px;
  }
</style>
</head>
<body>
<main class="canvas">
  <section class="card card--front" aria-label="Card front">
    <div class="info-panel">
      <div class="brand">
        <span class="brand__dot" aria-hidden="true"></span>
        <span class="brand__name">Evergreen<br>Nutrition &amp; Fitness</span>
      </div>
      <div class="contact">
        <p>Corinne Dalby Nutrition &amp; Fitness Coach for Seniors Private gym at : 17 Fennick Street, Brantwood, Perth, WA 6291 Mob : 0412736158</p>
        <p>Email : corinnedalby@fernpost.example</p>
        <p>"For Seniors by a Senior"</p>
      </div>
    </div>
  </section>

  <section class="card card--back" aria-label="Card back">
    <div class="credentials-frame">
      <p class="credentials">B.A. ( Soc.) Dip. Ed. (Sec.) Wellness Coach Cert 4 Personal Trainer Cert. Nutritition MOVE ON Facilitator Ageing Well Moving Freely Facilitator NLP Master</p>
    </div>
  </section>
</main>
</body>
</html>
```